VELKORIS Stationery Design Project

I want a stationery design for a web development company consists of:
1- business card
2- Letter Head
3- small Envelope
4- Large Envelope

need a very clean professional simple design yet creative,

The company logo is attached
http://www.pixelbazaarhub.net/project-progress/designs.aspx?briefId=5830174&submissionId=47210938

logo font is sui generis rg (attached)
I would like to have the stationery text font to be helvetica font regular or light (can be changed)

I love the combination of cyan, black and grey colors
( will attach some recommended styles)

Business

• curves or waves

```html
<!DOCTYPE html>
<html lang="en">
<head>
<meta charset="utf-8">
<title>VELKORIS Business Card</title>
<link rel="stylesheet" href="https://fonts.googleapis.com/css2?family=Orbitron:wght@500&family=Open+Sans:wght@400;600&display=swap">
<style>
  :root {
    --backdrop: #dcd9d5;
    --card: #161616;
    --card-edge: #0d0d0d;
    --cyan: #1ea0e6;
    --grey: #a7a9ac;
    --text: #e6e6e6;
    --emboss: #2b2b2b;
    --rule: #8a8a8a;
  }
  * { margin: 0; padding: 0; box-sizing: border-box; }
  html, body { width: 1200px; height: 1200px; overflow: hidden; }
  body {
    background: var(--backdrop);
    display: flex;
    flex-direction: column;
    align-items: center;
    justify-content: center;
    gap: 70px;
    font-family: "Open Sans", Helvetica, Arial, sans-serif;
  }
  .card {
    width: 760px;
    height: 434px;
    background: linear-gradient(135deg, #1c1c1c 0%, var(--card) 55%, var(--card-edge) 100%);
    border-radius: 6px;
    box-shadow: 0 14px 30px rgba(0,0,0,.28);
    position: relative;
  }
  .brand-name {
    font-family: "Orbitron", sans-serif;
    font-weight: 500;
    letter-spacing: 0.14em;
  }
  .card--front {
    display: flex;
    align-items: center;
    justify-content: center;
  }
  .card--front .brand-name {
    font-size: 58px;
    color: var(--emboss);
  }
  .card--back {
    display: flex;
    align-items: center;
    padding: 0 60px 0 70px;
  }
  .card--back .brand {
    width: 300px;
  }
  .card--back .brand-name {
    font-size: 36px;
    color: var(--cyan);
  }
  .divider {
    width: 1.5px;
    height: 190px;
    background: var(--rule);
    margin: 0 36px 0 20px;
  }
  .contact { color: var(--text); font-size: 17px; line-height: 1.45; }
  .contact .person-name {
    font-family: "Orbitron", sans-serif;
    color: var(--cyan);
    font-size: 21px;
    font-weight: 500;
  }
  .contact .role { font-size: 16px; margin-bottom: 10px; }
  .contact .address { margin-bottom: 10px; }
  .contact-line { display: flex; align-items: center; gap: 9px; }
  .contact-line svg { width: 15px; height: 15px; fill: var(--cyan); flex: none; }
</style>
</head>
<body>
  <section class="card card--front" aria-label="Business card front">
    <span class="brand-name">VELKORIS</span>
  </section>

  <section class="card card--back" aria-label="Business card back">
    <div class="brand"><span class="brand-name">VELKORIS</span></div>
    <div class="divider"></div>
    <div class="contact">
      <div class="person-name">Daniel Arwin</div>
      <div class="role">President</div>
      <div class="address">12 Harbor Lane, Eastfield<br>P.O. Box 214, 9 Crest Road</div>
      <div class="contact-line">
        <svg viewBox="0 0 24 24"><path d="M6.6 10.8a15.1 15.1 0 0 0 6.6 6.6l2.2-2.2a1 1 0 0 1 1-.25 11.4 11.4 0 0 0 3.6.57 1 1 0 0 1 1 1V20a1 1 0 0 1-1 1A17 17 0 0 1 3 4a1 1 0 0 1 1-1h3.5a1 1 0 0 1 1 1c0 1.25.2 2.45.57 3.57a1 1 0 0 1-.25 1z"/></svg>
        <span>555-0142-7788</span>
      </div>
      <div class="contact-line">
        <svg viewBox="0 0 24 24"><path d="M2 5h20v14H2z M2 5l10 8 10-8" fill="none" stroke="#1ea0e6" stroke-width="2.2"/></svg>
        <span>hello@velkorisweb.com</span>
      </div>
      <div class="contact-line">
        <svg viewBox="0 0 24 24"><circle cx="12" cy="12" r="9.5" fill="none" stroke="#1ea0e6" stroke-width="2"/><path d="M2.5 12h19M12 2.5c3 3 3 16 0 19M12 2.5c-3 3-3 16 0 19" fill="none" stroke="#1ea0e6" stroke-width="1.6"/></svg>
        <span>www.velkorisweb.com</span>
      </div>
    </div>
  </section>
</body>
</html>
```